Tamworth Logistics

Create a modern, simple, Elegant business card design for my business.

Services: Vexa Trucks, Transport, Contract Logistics,

Business

Include all details same as old card plus new website address: www.tamworthlogistics-demo.com.au

• Similar colors to Logo.

```html
<!DOCTYPE html>
<html lang="en">
<head>
<meta charset="utf-8">
<title>Tamworth Logistics – Business Card</title>
<link href="https://fonts.googleapis.com/css2?family=Montserrat:wght@400;500;700;800&display=swap" rel="stylesheet">
<style>
  :root {
    --navy: #0d4a7c;
    --navy-deep: #0a3d68;
    --sky: #2a8fd4;
    --ink: #2e2e2e;
    --grey: #8a8d91;
    --paper: #ffffff;
    --backdrop: #e9ebee;
  }
  * { box-sizing: border-box; margin: 0; padding: 0; }
  html, body { width: 1200px; height: 900px; overflow: hidden; }
  body {
    background: var(--backdrop);
    font-family: "Montserrat", sans-serif;
    position: relative;
  }
  .card {
    position: absolute;
    left: 300px;
    width: 600px;
    height: 343px;
    border-radius: 22px;
    overflow: hidden;
    box-shadow: 0 10px 28px rgba(0,0,0,.18);
  }

  /* Back side */
  .card-back { top: 80px; background: var(--navy); color: var(--paper); }
  .card-back .brand {
    position: absolute; left: 48px; top: 92px;
    font-weight: 800; font-size: 40px; line-height: 1.05;
    letter-spacing: .5px; color: var(--paper);
  }
  .card-back .brand-dot {
    display: inline-block; width: 12px; height: 12px;
    border-radius: 50%; background: var(--paper);
    margin-left: 6px; vertical-align: 4px;
  }
  .card-back .services {
    position: absolute; left: 300px; top: 120px; width: 270px;
    text-align: center; list-style: none;
    font-size: 14px; line-height: 1.45; font-weight: 400;
  }
  .card-back .web {
    position: absolute; left: 300px; width: 270px; top: 262px;
    text-align: center; font-size: 15px;
  }
  .web strong { font-weight: 700; }

  /* Front side */
  .card-front { top: 477px; background: var(--paper); }
  .card-front svg.bands { position: absolute; inset: 0; }
  .card-front .brand {
    position: absolute; left: 42px; top: 48px;
    font-weight: 800; font-size: 34px; line-height: 1.05;
    color: var(--grey);
  }
  .card-front .brand-dot {
    display: inline-block; width: 10px; height: 10px;
    background: var(--grey); margin-left: 6px; vertical-align: 3px;
  }
  .tagline {
    position: absolute; left: 42px; top: 160px;
    font-weight: 800; font-size: 17px; letter-spacing: .3px;
    color: var(--navy);
  }
  .person {
    position: absolute; right: 58px; top: 62px; text-align: right;
    border-bottom: 1.5px solid #555; padding: 0 0 5px 60px;
  }
  .person .name { font-weight: 700; font-size: 22px; color: var(--navy); }
  .person .role { font-size: 12px; color: var(--ink); }
  .contacts {
    position: absolute; left: 42px; top: 240px; width: 330px;
    border-top: 1.5px solid #555; padding-top: 8px;
    list-style: none; font-size: 14px; color: var(--ink);
  }
  .contacts li { display: flex; align-items: center; gap: 10px; line-height: 1.55; }
  .contacts svg { width: 12px; height: 12px; flex: none; }
</style>
</head>
<body>

<section class="card card-back">
  <div class="brand">Tamworth<br>Logistics<span class="brand-dot"></span></div>
  <ul class="services">
    <li>Vexa Trucks</li>
    <li>All General and Oversize Transport</li>
    <li>Specialized Transport</li>
    <li>Contract Logistics</li>
    <li>Express/Hotshot Services</li>
  </ul>
  <p class="web">www.<strong>tamworthlogistics-demo</strong>.com.au</p>
</section>

<section class="card card-front">
  <svg class="bands" viewBox="0 0 600 343" aria-hidden="true">
    <rect x="560" y="55" width="40" height="42" fill="var(--navy)"/>
    <polygon points="470,250 600,250 600,343 448,343" fill="var(--navy)"/>
    <polygon points="0,331 456,331 452,343 0,343" fill="var(--sky)"/>
  </svg>

  <div class="brand">Tamworth<br>Logistics<span class="brand-dot"></span></div>
  <p class="tagline">VEXA TRUCKS - TRANSPORT - CONTRACT LOGISTICS</p>

  <div class="person">
    <p class="name">Marcus Whitfield</p>
    <p class="role">Director</p>
  </div>

  <ul class="contacts">
    <li>
      <svg viewBox="0 0 24 24"><path fill="var(--navy)" d="M6.6 10.8a15 15 0 0 0 6.6 6.6l2.2-2.2a1 1 0 0 1 1-.25 11.4 11.4 0 0 0 3.6.57 1 1 0 0 1 1 1V20a1 1 0 0 1-1 1A17 17 0 0 1 3 4a1 1 0 0 1 1-1h3.5a1 1 0 0 1 1 1c0 1.25.2 2.45.57 3.6a1 1 0 0 1-.25 1z"/></svg>
      0400 555 182
    </li>
    <li>
      <svg viewBox="0 0 24 24"><rect x="2" y="5" width="20" height="14" rx="2" fill="none" stroke="var(--navy)" stroke-width="2.4"/><path d="M3 6l9 7 9-7" fill="none" stroke="var(--navy)" stroke-width="2.4"/></svg>
      marcus@tamworthlogistics-demo.com.au
    </li>
    <li>
      <svg viewBox="0 0 24 24"><circle cx="12" cy="12" r="10" fill="var(--navy)"/><path d="M2 12h20M12 2c3 3 3 17 0 20M12 2c-3 3-3 17 0 20" fill="none" stroke="#fff" stroke-width="1.5"/></svg>
      <span>www.<strong style="color:var(--navy)">tamworthlogistics-demo</strong>.com.au</span>
    </li>
  </ul>
</section>

</body>
</html>
```